Logo and business card design.

Looking for someone to design a simple logo and a business card.

Name of company: Corvane Waste Management
Logo symbol.. like attached Phoenix.

Colors: black/white/light green/ light blue.

Name on Card: Dale Marrow, President
Phone: 212.384.9057
Other info: 24 Hour Service | Fully Insured

```html
<!DOCTYPE html>
<html lang="en">
<head>
<meta charset="utf-8">
<title>Corvane Waste Management – Business Card</title>
<link href="https://fonts.googleapis.com/css2?family=Roboto:wght@300;400;500;700&display=swap" rel="stylesheet">
<style>
  :root {
    --backdrop: #2b2d31;
    --card: #050505;
    --ink: #ffffff;
    --ink-soft: #d9d9d9;
    --accent-blue: #2fa4dc;
  }
  * { margin: 0; padding: 0; box-sizing: border-box; }
  html, body {
    width: 1200px; height: 900px; overflow: hidden;
    background: var(--backdrop);
    font-family: "Roboto", Arial, sans-serif;
    color: var(--ink);
  }
  .stage { position: relative; width: 1200px; height: 900px; }
  .card {
    position: absolute; width: 600px; height: 343px;
    background: var(--card); border-radius: 4px;
    box-shadow: 0 14px 30px rgba(0,0,0,.45);
  }
  .card--front { left: 540px; top: 70px; }
  .card--back  { left: 60px;  top: 480px; }

  .brand { display: flex; align-items: center; gap: 16px; }
  .brand__mark { width: 46px; height: 46px; border-radius: 50%; background: var(--accent-blue); flex: none; }
  .brand__name { color: var(--ink); font-weight: 400; line-height: 1.05; }
  .brand__name span { display: block; }
  .brand__primary { font-size: 58px; }
  .brand__secondary { font-size: 22px; letter-spacing: 2px; }

  .card--front .brand { position: absolute; left: 110px; top: 112px; }

  .card--back .brand { position: absolute; left: 34px; top: 34px; gap: 12px; }
  .card--back .brand__mark { width: 34px; height: 34px; }
  .card--back .brand__primary { font-size: 38px; }
  .card--back .brand__secondary { font-size: 14px; letter-spacing: 1.6px; }

  .tagline { position: absolute; left: 34px; top: 132px; font-size: 15px; color: var(--ink); }

  .person { position: absolute; right: 34px; top: 38px; text-align: right; }
  .person__name { font-size: 26px; font-weight: 700; }
  .person__title { font-size: 17px; font-weight: 400; margin-top: 2px; }

  .contacts { position: absolute; left: 240px; top: 150px; list-style: none; }
  .contacts li { display: flex; align-items: center; gap: 12px; margin-bottom: 12px; color: var(--ink-soft); font-size: 13px; }
  .contacts svg { width: 22px; height: 22px; flex: none; stroke: var(--ink); fill: none; stroke-width: 1.6; }
  .contacts .contacts__phone { font-size: 27px; color: var(--ink); letter-spacing: 1px; }
  .contacts .contacts__phone svg { width: 30px; height: 30px; }
  .contacts .contacts__web { font-size: 15px; color: var(--ink); }
</style>
</head>
<body>
<main class="stage">
  <section class="card card--front" aria-label="Card front">
    <div class="brand">
      <div class="brand__mark"></div>
      <p class="brand__name"><span class="brand__primary">Corvane</span><span class="brand__secondary">Waste Management</span></p>
    </div>
  </section>

  <section class="card card--back" aria-label="Card back">
    <div class="brand">
      <div class="brand__mark"></div>
      <p class="brand__name"><span class="brand__primary">Corvane</span><span class="brand__secondary">Waste Management</span></p>
    </div>
    <p class="tagline">24 Hour Service | Fully Insured</p>

    <div class="person">
      <p class="person__name">Dale Marrow</p>
      <p class="person__title">President</p>
    </div>

    <ul class="contacts">
      <li class="contacts__phone">
        <svg viewBox="0 0 24 24"><circle cx="12" cy="12" r="10.5"/><path d="M9 7.5c-.8.4-1.3 1.2-1 2.3.8 2.6 2.8 4.7 5.3 5.6 1.1.3 1.9-.2 2.3-1l-1.7-1.4-1.1.8c-1.1-.6-2-1.5-2.6-2.6l.8-1.1z"/></svg>
        212.384.9057
      </li>
      <li>
        <svg viewBox="0 0 24 24"><path d="M12 22s-7-7.2-7-12a7 7 0 0 1 14 0c0 4.8-7 12-7 12z"/><circle cx="12" cy="10" r="2.6"/></svg>
        City Name, Road Name, Street No
      </li>
      <li>
        <svg viewBox="0 0 24 24"><rect x="2.5" y="5" width="19" height="14"/><path d="M2.5 5l9.5 8 9.5-8"/></svg>
        info@yourmail.com
      </li>
      <li class="contacts__web">
        <svg viewBox="0 0 24 24"><circle cx="12" cy="12" r="9.5"/><ellipse cx="12" cy="12" rx="4" ry="9.5"/><path d="M2.5 12h19M4 7h16M4 17h16"/></svg>
        www.yousite.com
      </li>
    </ul>
  </section>
</main>
</body>
</html>
```